Business Card Design

I need a business card design for my law office based in Pasadena, California. I am a sole practitioner and I specialize in business transaction and litigation, probate and estate planning, taxation law, corporate and business formation, immigration and real estate. I want something that is simple, yet stands out.

A friend helped to create a logo about 6 years ago. I am open to new ideas to changing the logo.

Industry/Entity Type

Business

Contact Information for Business Card

Law Offices of Dorvan L. Mabry
842 W. Larkspur Ave., Suite 319
Pasadena, CA 90287
Tel: 626-555-0174
Fax: 626-555-0139
Email: dmabry@dlmlegalgroup.example

Attorney: Dorvan L. Mabry

```html
<!DOCTYPE html>
<html lang="en">
<head>
<meta charset="utf-8">
<title>Law Offices of Dorvan L. Mabry – Business Cards</title>
<link rel="stylesheet" href="https://fonts.googleapis.com/css2?family=Cinzel:wght@500&family=Arimo:wght@400;700&display=swap">
<style>
  :root {
    --page: #e4e2de;
    --ink-black: #1b1b1b;
    --ink-charcoal: #2c2c2c;
    --band-dark: #222222;
    --band-light: #5a5a5a;
    --paper: #ffffff;
    --text-grey: #6e6e6e;
    --rule-grey: #9a9a9a;
    --white: #ffffff;
  }
  * { box-sizing: border-box; margin: 0; padding: 0; }
  html, body { width: 1200px; height: 950px; overflow: hidden; }
  body {
    background: var(--page);
    font-family: "Arimo", Arial, sans-serif;
    position: relative;
  }
  .card {
    position: absolute;
    left: 250px;
    width: 700px;
    height: 400px;
    box-shadow: 0 6px 18px rgba(0,0,0,.22);
    overflow: hidden;
  }

  /* Back of card */
  .card-back {
    top: 50px;
    background: linear-gradient(135deg, var(--ink-charcoal) 0%, var(--ink-black) 60%, #111 100%);
    color: var(--white);
  }
  .back-mark {
    position: absolute;
    left: 0; right: 0; top: 140px;
    display: flex; align-items: center; justify-content: center; gap: 18px;
  }
  .back-mark .square {
    width: 34px; height: 34px;
    border: 2px solid var(--white);
  }
  .back-mark .name {
    font-family: "Cinzel", Georgia, serif;
    font-weight: 500;
    font-size: 40px;
    letter-spacing: 2px;
    color: var(--white);
  }
  .back-web {
    position: absolute;
    left: 0; right: 0; top: 300px;
    text-align: center;
    font-size: 15px;
    letter-spacing: 3px;
    color: var(--white);
  }

  /* Front of card */
  .card-front {
    top: 500px;
    background: var(--paper);
  }
  .firm-lockup {
    position: absolute;
    left: 40px; top: 34px;
    display: flex; align-items: flex-end; gap: 14px;
    font-family: "Cinzel", Georgia, serif;
    font-weight: 500;
    color: var(--ink-black);
  }
  .firm-lockup .square {
    width: 46px; height: 46px;
    border: 2px solid var(--ink-black);
    margin-bottom: 6px;
  }
  .firm-lockup .words { display: flex; flex-direction: column; }
  .firm-lockup .lead {
    font-size: 10px;
    letter-spacing: 4px;
    padding-bottom: 5px;
    border-bottom: 1px solid var(--rule-grey);
  }
  .firm-lockup .firm-name {
    font-size: 28px;
    letter-spacing: 1px;
    padding-top: 6px;
  }
  .band {
    position: absolute;
    left: 0; right: 0; top: 160px;
    height: 74px;
    background: linear-gradient(90deg, var(--band-dark) 0%, var(--band-dark) 45%, var(--band-light) 72%, var(--band-dark) 100%);
  }
  .band .person {
    position: absolute; left: 40px; top: 14px;
    color: var(--white);
  }
  .band .person-name { font-weight: 700; font-size: 22px; }
  .band .person-title { font-size: 15px; margin-top: 4px; color: #e6e6e6; }
  .band .band-mark {
    position: absolute; right: 40px; top: 22px;
    font-family: "Cinzel", Georgia, serif;
    font-weight: 500;
    font-size: 22px;
    color: var(--white);
  }
  .address {
    position: absolute;
    left: 40px; top: 272px;
    font-style: normal;
    font-size: 18px;
    line-height: 1.4;
    color: var(--text-grey);
  }
  .contacts {
    position: absolute;
    left: 400px; top: 268px;
    list-style: none;
    font-size: 17px;
    color: var(--text-grey);
  }
  .contacts li { display: flex; align-items: center; gap: 12px; height: 30px; }
  .contacts svg { width: 18px; height: 18px; fill: var(--ink-black); flex: none; }
</style>
</head>
<body>

  <section class="card card-back" aria-label="Card back">
    <div class="back-mark">
      <span class="square"></span>
      <span class="name">Dorvan L. Mabry</span>
    </div>
    <p class="back-web">www.dlmlegalgroup.example</p>
  </section>

  <section class="card card-front" aria-label="Card front">
    <div class="firm-lockup">
      <span class="square"></span>
      <div class="words">
        <span class="lead">LAW OFFICES OF</span>
        <span class="firm-name">DORVAN L. MABRY</span>
      </div>
    </div>

    <div class="band">
      <div class="person">
        <p class="person-name">Dorvan L. Mabry</p>
        <p class="person-title">CEO/Founder</p>
      </div>
      <span class="band-mark">Dorvan L. Mabry</span>
    </div>

    <address class="address">
      842 W. Larkspur Ave.,<br>
      Suite 319<br>
      Pasadena, CA 90287
    </address>

    <ul class="contacts">
      <li>
        <svg viewBox="0 0 24 24" aria-hidden="true"><path d="M6.6 10.8a15.5 15.5 0 0 0 6.6 6.6l2.2-2.2c.3-.3.7-.4 1-.2 1.1.4 2.3.6 3.6.6.6 0 1 .4 1 1V20c0 .6-.4 1-1 1A17 17 0 0 1 3 4c0-.6.4-1 1-1h3.5c.6 0 1 .4 1 1 0 1.3.2 2.5.6 3.6.1.3 0 .7-.2 1z"/></svg>
        626-555-0174
      </li>
      <li>
        <svg viewBox="0 0 24 24" aria-hidden="true"><path d="M7 3h10v5H7zM4 9h16a2 2 0 0 1 2 2v6h-4v4H6v-4H2v-6a2 2 0 0 1 2-2zm4 7v3h8v-3z"/></svg>
        626-555-0139
      </li>
      <li>
        <svg viewBox="0 0 24 24" aria-hidden="true"><path d="M2 5h20v14H2zm2 2v.5l8 5 8-5V7l-8 5z"/></svg>
        dmabry@dlmlegalgroup.example
      </li>
    </ul>
  </section>

</body>
</html>
```